New Managed IT company needs a business card

We are an IT management and support company that needs a business card design. I have a logo that I'll provide. Blues and blacks match the logo, but i'm open to anything. I want the card to help people take us seriously, but still have some energy and fun in it. The card should communicate stability and a solid company.

Target Market(s)

Target market includes Owners and Presidents at small businesses of 20 - 100 employees in the Pittsburgh PA area.

Industry/Entity Type

Information Technology

Contact Information for Business Card

i am open to other designs, but i imagine having only the logo on one side and then the logo plus all contact details on the other side.

Requirements
Must have
• Our logo
• Company name is optional if the logo makes it obvious
• A name - Lew Tasker
• A title - President
• A phone number - 724-XXX-XXXX
• A mobile phone number - 724-516-0471
• An email address - ltasker@brightlanetech.com
• a website - brightlanetech.com or www.brightlanetech.com
Nice to have
• some people tell me the logo feels like a superhero theme, some fun with that idea might be good. I'm open to ideas.
Should not have
• stock photos of people or computers - especially old looking stuff.

```html
<!DOCTYPE html>
<html lang="en">
<head>
<meta charset="utf-8">
<title>Brightlane Tech – Business Card</title>
<link rel="stylesheet" href="https://fonts.googleapis.com/css2?family=Michroma&family=Nunito:wght@400;600;800&display=swap">
<style>
  :root {
    --backdrop: #e7e4df;
    --card-light: #f3f3f3;
    --card-dark: #2a2a2c;
    --ink: #1e1e20;
    --blue: #1680cf;
    --blue-deep: #0b4c9c;
    --silver: #d2d2d2;
  }
  html, body {
    margin: 0;
    width: 1200px;
    height: 443px;
    overflow: hidden;
    background: var(--backdrop);
  }
  .canvas {
    position: relative;
    width: 1200px;
    height: 443px;
  }
  .card {
    position: absolute;
    top: 90px;
    width: 490px;
    height: 276px;
    border-radius: 14px;
    overflow: hidden;
  }
  .card--front { left: 108px; background: var(--card-light); }
  .card--back  { left: 602px; background: var(--card-dark); }
  .card__disc {
    position: absolute;
    top: 0;
    left: 0;
  }
  .brand-small {
    position: absolute;
    left: 24px;
    top: 16px;
  }
  .brand-small__dot {
    display: block;
    width: 28px;
    height: 28px;
    margin-left: 28px;
    border-radius: 50%;
    background: var(--blue);
  }
  .brand-small__name {
    display: block;
    margin-top: 6px;
    font-family: "Michroma", sans-serif;
    font-size: 8px;
    letter-spacing: 0.5px;
    color: var(--ink);
  }
  .person {
    position: absolute;
    left: 24px;
    top: 133px;
  }
  .person__name {
    margin: 0;
    font-family: "Michroma", sans-serif;
    font-size: 15px;
    letter-spacing: 1.5px;
    color: var(--ink);
    text-transform: uppercase;
  }
  .person__title {
    margin: 3px 0 0;
    font-family: "Nunito", sans-serif;
    font-weight: 800;
    font-size: 10px;
    letter-spacing: 1.6px;
    color: var(--blue-deep);
  }
  .contact {
    position: absolute;
    left: 26px;
    top: 174px;
    margin: 0;
    padding: 0;
    list-style: none;
    font-family: "Nunito", sans-serif;
    font-size: 12px;
    color: #333;
  }
  .contact__row {
    display: flex;
    align-items: center;
    height: 19px;
  }
  .contact__icon {
    width: 13px;
    height: 13px;
    margin-right: 15px;
    flex: none;
  }
  .brand-large {
    position: absolute;
    left: 246px;
    top: 124px;
    width: 220px;
    text-align: center;
  }
  .brand-large__dot {
    display: block;
    width: 58px;
    height: 58px;
    margin: 0 auto;
    border-radius: 50%;
    background: var(--blue);
  }
  .brand-large__name {
    display: block;
    margin-top: 18px;
    font-family: "Michroma", sans-serif;
    font-size: 15px;
    letter-spacing: 1px;
    color: var(--silver);
    white-space: nowrap;
  }
</style>
</head>
<body>
<main class="canvas">

  <section class="card card--front" aria-label="Card front">
    <svg class="card__disc" width="490" height="276" aria-hidden="true">
      <defs>
        <linearGradient id="disc-dark" x1="0" y1="0" x2="0" y2="1">
          <stop offset="0" stop-color="#4a4a4d"/>
          <stop offset="1" stop-color="#0e0e10"/>
        </linearGradient>
      </defs>
      <circle cx="496" cy="138" r="132" fill="url(#disc-dark)"/>
    </svg>

    <div class="brand-small">
      <span class="brand-small__dot"></span>
      <span class="brand-small__name">BRIGHTLANE TECH</span>
    </div>

    <div class="person">
      <h1 class="person__name">Lew Tasker</h1>
      <p class="person__title">PRESIDENT</p>
    </div>

    <ul class="contact">
      <li class="contact__row">
        <svg class="contact__icon" viewBox="0 0 16 16" aria-hidden="true"><path fill="var(--blue)" d="M1 6c0-2 3-4 7-4s7 2 7 4l-3 1-1-2H5L4 7 1 6zm3 2h8l2 6H2l2-6zm4 1.5a2 2 0 100 4 2 2 0 000-4z"/></svg>
        <span>724-XXX-XXXX</span>
      </li>
      <li class="contact__row">
        <svg class="contact__icon" viewBox="0 0 16 16" aria-hidden="true"><rect x="4" y="1" width="8" height="14" rx="1.5" fill="none" stroke="var(--blue)" stroke-width="1.6"/><circle cx="8" cy="12.5" r="0.9" fill="var(--blue)"/></svg>
        <span>724-516-0471</span>
      </li>
      <li class="contact__row">
        <svg class="contact__icon" viewBox="0 0 16 16" aria-hidden="true"><rect x="1" y="3" width="14" height="10" rx="1" fill="var(--blue)"/><path d="M1.5 3.5L8 9l6.5-5.5" fill="none" stroke="#fff" stroke-width="1.2"/></svg>
        <span>ltasker@brightlanetech.com</span>
      </li>
      <li class="contact__row">
        <svg class="contact__icon" viewBox="0 0 16 16" aria-hidden="true"><g fill="none" stroke="var(--blue)" stroke-width="1.3"><circle cx="8" cy="8" r="6.5"/><ellipse cx="8" cy="8" rx="2.8" ry="6.5"/><path d="M1.5 8h13M2.5 4.5h11M2.5 11.5h11"/></g></svg>
        <span>www.brightlanetech.com</span>
      </li>
    </ul>
  </section>

  <section class="card card--back" aria-label="Card back">
    <svg class="card__disc" width="490" height="276" aria-hidden="true">
      <defs>
        <linearGradient id="disc-light" x1="0" y1="0" x2="0" y2="1">
          <stop offset="0" stop-color="#d6d6d6"/>
          <stop offset="1" stop-color="#e8e8e8"/>
        </linearGradient>
      </defs>
      <circle cx="-6" cy="138" r="132" fill="url(#disc-light)"/>
    </svg>

    <div class="brand-large">
      <span class="brand-large__dot"></span>
      <span class="brand-large__name">BRIGHTLANE TECH</span>
    </div>
  </section>

</main>
</body>
</html>
```